Flyer Design Project

I need to create a flyer to advertise an Luxury Self Catering Apartment Complex in a Ski Resort in Europe. The development offers luxury accommodation to those who are on a budget.

Below is what needs to be included and a basic layout design idea i had that can be changed. The information is important. Hoping to get it on a flyer sized 21.6 x 14 cm

Title - 'Luxury Self Catering Ski Apartments For Rent'
Sub Title - 'Located 200m from Gondola, Restaurants and Bars'

Studio - Sleeps 1-2 - From only £200 per week
1 Bed - Sleeps 2-4 - From only £250 per week
2 Bed - Sleeps 4-6 - From only £350 per week

Image 1 Image 2 Image 3

- Fully Furnished Modern, Spacious & Comfortable Apartments
- Fully Staffed Development (Reception, Bar + Daily Cleaning)
- Family friendly & suitable for children of all ages

(Twitter Icon) @snowlarkchalets
E-mail - snowlarkchalets@mailvora.co.uk
Telephone - +44 (0) 7811 302 684

Target Market(s)

Our target market is very wide. We are trying to attract students, couples and families who are skiing on a budget.

Industry/Entity Type

Accommodation

Requirements
Must have
• The text contained in 'task description' is important but i'd like to be led on design. Size of around 21.6 x 14cm is important and i'd like the 3 images below (hopefully someone can get of the date and time in orange bottom right of all pics)

http://i2217.picvaultra.com/albums/kq412/tmwimages/Bansko/699_00_640_zpsd7b2ba81.jpeg

http://i2217.picvaultra.com/albums/kq412/tmwimages/Bansko/a_02_zps7503dd10.jpeg

http://i2217.picvaultra.com/albums/kq412/tmwimages/Bansko/699_08_640_zps2f11bf21.jpeg

```html
<!DOCTYPE html>
<html lang="en">
<head>
<meta charset="utf-8">
<title>Luxury Self Catering Ski Apartments For Rent</title>
<link rel="stylesheet" href="https://fonts.googleapis.com/css2?family=Sniglet:wght@400;800&display=swap">
<style>
  :root {
    --ink: #1f1f2a;
    --navy: #4b4c8c;
    --sky: #8ccbef;
    --icon: #29a9e8;
    --snow-light: #f3f5f9;
    --snow-mid: #dde3ec;
    --snow-shade: #c4ccd8;
  }
  * { margin: 0; padding: 0; box-sizing: border-box; }
  html, body { width: 1200px; height: 778px; overflow: hidden; background: #fff; }
  .flyer {
    position: relative;
    width: 1200px;
    height: 778px;
    overflow: hidden;
    font-family: "Sniglet", "Trebuchet MS", sans-serif;
    color: var(--ink);
  }
  .backdrop {
    position: absolute; inset: 0;
    background:
      radial-gradient(ellipse 700px 300px at 1000px 200px, var(--snow-shade), transparent 70%),
      radial-gradient(ellipse 500px 260px at 250px 330px, var(--snow-mid), transparent 70%),
      linear-gradient(180deg, var(--snow-mid) 0%, var(--snow-light) 45%, #fafbfd 100%);
  }
  .side-strip {
    position: absolute; left: 0; top: 0; width: 152px; height: 778px;
    background: rgba(255,255,255,0.35);
  }
  .resort-name {
    position: absolute;
    left: 152px; top: 778px;
    transform-origin: 0 0;
    transform: rotate(-90deg);
    width: 778px;
    font-weight: 800;
    font-size: 196px;
    line-height: 152px;
    letter-spacing: 6px;
    color: var(--sky);
    opacity: 0.85;
    white-space: nowrap;
    transform: rotate(-90deg) translateY(-152px);
  }
  .title {
    position: absolute; left: 190px; top: 40px;
    font-weight: 800;
    font-size: 62px;
    line-height: 80px;
    color: var(--navy);
  }
  .subtitle {
    position: absolute; left: 190px; top: 214px;
    font-size: 27px;
    font-weight: 400;
  }
  .gallery {
    position: absolute; left: 187px; top: 273px;
    display: flex; gap: 11px;
  }
  .gallery .photo {
    width: 201px; height: 137px;
    border: 5px solid var(--navy);
    border-radius: 6px 22px 6px 22px;
  }
  .photo.building { background: linear-gradient(180deg, #cfd9e6 0%, #a78d74 55%, #5e5048 100%); }
  .photo.bedroom { background: linear-gradient(135deg, #6a4a2c 0%, #c79a5c 50%, #e6d8c4 100%); }
  .photo.lounge { background: linear-gradient(180deg, #b7a38a 0%, #efe9df 40%, #5a3b25 100%); }
  .photo.kitchen { background: linear-gradient(180deg, #e8e3da 0%, #a48d74 50%, #4a3222 100%); }
  .rates {
    position: absolute; left: 190px; top: 436px;
    list-style: none;
    font-size: 25px;
    line-height: 39px;
  }
  .features {
    position: absolute; left: 190px; top: 578px;
    list-style: none;
    font-size: 21px;
    line-height: 32px;
  }
  .features li::before {
    content: "";
    display: inline-block;
    width: 15px; height: 15px;
    margin-right: 8px;
    background: var(--navy);
    border-radius: 2px;
    vertical-align: -1px;
  }
  .contacts {
    position: absolute; left: 192px; top: 701px;
    display: flex; align-items: center;
    font-size: 21px;
  }
  .contacts .item { display: flex; align-items: center; gap: 6px; margin-right: 26px; }
  .contacts .marker {
    width: 43px; height: 43px;
    background: var(--icon);
    border-radius: 8px;
  }
</style>
</head>
<body>
  <div class="flyer">
    <div class="backdrop" role="img" aria-label="Snow-covered ski slope with pine trees under a pale winter sky"></div>
    <div class="side-strip"></div>
    <div class="resort-name" aria-hidden="true">BANSKO</div>

    <h1 class="title">Luxury Self Catering<br>Ski Apartments For Rent</h1>
    <p class="subtitle">Located 200m from Gondola, Restaurants and Bars</p>

    <div class="gallery">
      <div class="photo building" role="img" aria-label="Stone and render apartment building exterior"></div>
      <div class="photo bedroom" role="img" aria-label="Warmly lit double bedroom"></div>
      <div class="photo lounge" role="img" aria-label="Living room with sofa and tall windows"></div>
      <div class="photo kitchen" role="img" aria-label="Open-plan kitchen and dining area"></div>
    </div>

    <ul class="rates">
      <li>Studio - Sleeps 1-2 - From only £200 per week</li>
      <li>1 Bed - Sleeps 2-4 - From only £250 per week</li>
      <li>2 Bed - Sleeps 4-6 - From only £350 per week</li>
    </ul>

    <ul class="features">
      <li>Fully Furnished Modern, Spacious &amp; Comfortable Apartments</li>
      <li>Fully Staffed Development (Reception, Bar + Daily Cleaning)</li>
      <li>Family friendly &amp; suitable for children of all ages</li>
    </ul>

    <div class="contacts">
      <div class="item"><span class="marker"></span><span>@snowlarkchalets</span></div>
      <div class="item"><span class="marker"></span><span>snowlarkchalets@mailvora.co.uk</span></div>
      <div class="item"><span class="marker"></span><span>+44 (0) 7811 302 684</span></div>
    </div>
  </div>
</body>
</html>
```